Morning Harvest Psalm Journal for the Weary Traveler on the Narrow Road

This is not an Eastern meditation method. No images or themes from guru style or Eastern meditations from Hinduism or Buddhism will work. This is a Biblical Christian-based method. Some sort of Divine Light from Heaven may be the look. Some "ancient scroll" for the title to be written in may work.

```html
<!DOCTYPE html>
<html lang="en">
<head>
<meta charset="utf-8">
<title>Morning Harvest Psalm Journal for the Weary Traveler on the Narrow Road</title>
<link rel="stylesheet" href="https://fonts.googleapis.com/css2?family=Permanent+Marker&family=Libre+Baskerville&display=swap">
<style>
  :root {
    --backdrop: #ececec;
    --ink-navy: #0f2456;
    --ink-black: #1a1410;
    --sky-pink: #eeaa9c;
    --sky-rose: #e3a2b0;
    --sun-glow: #fff8e0;
    --sand-light: #f1dcb8;
    --sand-deep: #dcbf8e;
  }
  * { margin: 0; padding: 0; box-sizing: border-box; }
  html, body {
    width: 1200px;
    height: 800px;
    overflow: hidden;
    background: var(--backdrop);
  }
  .canvas {
    position: relative;
    width: 1200px;
    height: 800px;
  }
  .cover {
    position: absolute;
    left: 400px;
    top: 95px;
    width: 400px;
    height: 610px;
    overflow: hidden;
  }
  .cover-art {
    position: absolute;
    inset: 0;
    background:
      radial-gradient(ellipse 150px 120px at 140px 50px, var(--sun-glow) 0%, rgba(255,244,214,0.75) 40%, rgba(255,230,200,0) 100%),
      radial-gradient(ellipse 260px 220px at 150px 70px, rgba(255,228,196,0.7) 0%, rgba(255,220,190,0) 100%),
      linear-gradient(180deg, var(--sky-rose) 0%, var(--sky-pink) 38%, #eec2a8 52%, var(--sand-light) 62%, #ecd2a6 80%, var(--sand-deep) 100%);
  }
  .cover-spine {
    position: absolute;
    left: 6px;
    top: 0;
    width: 4px;
    height: 100%;
    background: linear-gradient(90deg, rgba(0,0,0,0.06), rgba(255,255,255,0.35), rgba(0,0,0,0.04));
  }
  .cover-title {
    position: absolute;
    left: 0;
    right: 0;
    top: 60px;
    text-align: center;
    font-family: "Permanent Marker", cursive;
    color: var(--ink-navy);
    font-size: 58px;
    line-height: 92px;
    letter-spacing: 1px;
    text-transform: uppercase;
  }
  .cover-title span { display: block; }
  .cover-subtitle {
    position: absolute;
    left: 0;
    right: 0;
    top: 492px;
    text-align: center;
    font-family: "Libre Baskerville", serif;
    color: var(--ink-black);
    font-size: 17px;
    line-height: 29px;
    text-transform: uppercase;
  }
  .cover-subtitle span { display: block; }
</style>
</head>
<body>
  <main class="canvas">
    <article class="cover">
      <div class="cover-art" role="img" aria-label="Rays of heavenly light breaking through a pink sky above soft desert sand dunes"></div>
      <div class="cover-spine"></div>
      <h1 class="cover-title">
        <span>Morning</span>
        <span>Harvest</span>
        <span>Psalm</span>
        <span>Journal</span>
      </h1>
      <p class="cover-subtitle">
        <span>For the Weary Traveler</span>
        <span>on the Narrow Road</span>
      </p>
    </article>
  </main>
</body>
</html>
```